Lumentide

We have already had a logo designed. Attached is the logo.
We are now wanting to design a label that will wrap around a plastic bottle which contains 1 litre of fluid. The size of the label is 15cm high by 28 cm wide.
The bottle for which the label will be used is a natural wellbeing supplement in a class of its own. It is a liquid tonic/complementary medicine - not a drink you guzzle down like zestorade.
The label needs to look natural and healthy and include the logo attached.
This is a premium bottle which will cost more than $50 AUD per bottle. The label needs to be classy as you would expect to find on an expensive bottle of wine.
The label needs to be able to sell the bottle and it needs to convince that what is inside the bottle is worth what it will cost.
The product does not have fruit in it and is not a water drink. One of the ingredients is an extract from the French Maritime Pine Bark.
We do not want the label to be to busy.
The product is to market in China, United States and Australia.
We will have to typeset certain wording onto the label - Ingredients, company details, bottle code etc which will be on the back of the bottle.
Updates

We have uploaded a picture of the plastic bottle that the label will be used on. The dimensions of the label have been included in the project brief.

Regards

Reason: We realise that the time period allowed to create a label may have been to short for some designers. Thanks

Reason: Just waiting on final designs to be submitted. This will be the last extension. Regards

Target Market(s)

Generally adults aged 35 to 65.

Industry/Entity Type

Plastic

Requirements
Must have
• Most of this information has been outlined above.

```html
<!DOCTYPE html>
<html lang="en">
<head>
<meta charset="utf-8">
<title>Lumentide – Bottle Label</title>
<link rel="stylesheet" href="https://fonts.googleapis.com/css2?family=Montserrat:wght@600&family=Arimo:wght@400;700&display=swap">
<style>
  :root {
    --sea: #7ccbc0;
    --cream: #fdf8c8;
    --dash: #9fcfc2;
    --green: #1b7a3f;
    --red: #e0312b;
    --red-dark: #a8201c;
    --ink: #1a1a1a;
    --white: #ffffff;
  }
  * { margin: 0; padding: 0; box-sizing: border-box; }
  html, body { width: 1200px; height: 642px; overflow: hidden; background: var(--sea); }
  .label {
    position: relative; width: 1200px; height: 642px; background: var(--sea);
    font-family: "Arimo", Arial, sans-serif; color: var(--ink);
  }
  .ingredients-strip {
    position: absolute; left: 50px; top: 58px;
    writing-mode: vertical-rl; font-size: 12.5px; letter-spacing: 0.3px;
  }
  .ingredients-strip .heading { font-size: 8px; text-transform: uppercase; letter-spacing: 0.5px; }
  .panel { position: absolute; background: var(--cream); border-radius: 38px; }
  .panel::after {
    content: ""; position: absolute; inset: 9px; border: 1.5px dashed var(--dash); border-radius: 30px;
  }
  .nutrition-panel { left: 94px; top: 33px; width: 228px; height: 587px; padding: 42px 0 0 18px; }
  .nutrition-title { font-size: 17px; font-weight: 400; letter-spacing: 0.3px; line-height: 20px; }
  .nutrition-line { font-size: 12px; line-height: 14px; }
  .nutrition-rule { width: 166px; height: 5px; background: var(--ink); margin-top: 4px; }
  .story-panel { left: 899px; top: 33px; width: 261px; height: 247px; padding: 26px 20px 0 33px; }
  .story-title { font-size: 10px; font-weight: 400; text-transform: uppercase; line-height: 18px; }
  .story-title .brand { color: var(--green); font-size: 15px; }
  .story-text { font-size: 12.4px; line-height: 17px; position: relative; z-index: 1; }
  .front { position: absolute; left: 0; top: 0; width: 1200px; height: 642px; }
  .brand-name {
    position: absolute; left: 330px; width: 520px; top: 258px; text-align: center;
    font-family: "Montserrat", "Century Gothic", sans-serif; font-weight: 600;
    font-size: 72px; color: var(--green); letter-spacing: 0.5px;
  }
  .natural-text {
    position: absolute; left: 430px; width: 320px; top: 482px; text-align: center;
    color: var(--white); font-size: 22px; letter-spacing: 0.5px;
  }
  .natural-text .percent { font-size: 30px; }
</style>
</head>
<body>
<main class="label">
  <p class="ingredients-strip"><span class="heading">Ingredients:</span> pine bark extract, herbal tonic base, honey</p>

  <section class="panel nutrition-panel">
    <h2 class="nutrition-title">NUTRITION FACTS</h2>
    <p class="nutrition-line">Serving Size:</p>
    <p class="nutrition-line">Serving Per Container 1</p>
    <div class="nutrition-rule"></div>
  </section>

  <svg class="front" width="1200" height="642" viewBox="0 0 1200 642">
    <defs>
      <linearGradient id="fruitTones" x1="0" y1="0" x2="1" y2="0">
        <stop offset="0" stop-color="#e2413a"/>
        <stop offset="0.35" stop-color="#a9c04a"/>
        <stop offset="0.6" stop-color="#f2a33a"/>
        <stop offset="0.85" stop-color="#b7cf6a"/>
        <stop offset="1" stop-color="#c9302c"/>
      </linearGradient>
      <linearGradient id="leafTones" x1="0" y1="0" x2="1" y2="1">
        <stop offset="0" stop-color="#2e8f47"/>
        <stop offset="1" stop-color="#1b6b36"/>
      </linearGradient>
    </defs>
    <path class="front-badge" d="M590 93 L857 60 L852 355 A262 262 0 1 1 590 93 Z"
          fill="var(--cream)" stroke="var(--green)" stroke-width="15" stroke-linejoin="round"/>
    <rect role="img" aria-label="Two green leaves" x="694" y="88" width="90" height="66" rx="30" fill="url(#leafTones)"/>
    <circle class="brand-dot" cx="590" cy="215" r="34" fill="var(--green)"/>
    <rect role="img" aria-label="Illustration of fresh produce arranged along the badge"
          x="378" y="350" width="424" height="130" rx="40" fill="url(#fruitTones)"/>
    <g class="ribbon">
      <path d="M425 478 L460 478 L460 528 L425 528 L440 503 Z" fill="var(--red-dark)"/>
      <path d="M755 478 L720 478 L720 528 L755 528 L740 503 Z" fill="var(--red-dark)"/>
      <rect x="445" y="470" width="290" height="52" fill="var(--red)"/>
    </g>
  </svg>

  <h1 class="brand-name">Lumentide</h1>
  <p class="natural-text"><span class="percent">100 %</span> NATURAL</p>

  <section class="panel story-panel">
    <h2 class="story-title">Why <span class="brand">Lumentide?</span></h2>
    <p class="story-text">What is so good about LUMENTIDE healthy tonic, you ask? Well this tonic blends French maritime pine bark extract with pure botanicals to support calm, balance and lasting vitality. Made in small batches with care, every measured glass delivers clean, steady goodness you can trust.</p>
  </section>
</main>
</body>
</html>
```